Front signage

Our work consists of Industrial Electrical Automation.
We are an established company with a logo we are happy with.
Though we still need:
- a sign for our front door - 420mm x 1200mm
- a sign at the front of the building - 250mm x 1600mm

Please see attached our logo, and following our colour theme would be nice, but not essential.
Please see our website for more information on what we do
www.voltarispan.com.au

```html
<!DOCTYPE html>
<html lang="en">
<head>
<meta charset="utf-8">
<title>Voltaris Span Services – Front Signage</title>
<link href="https://fonts.googleapis.com/css2?family=Archivo+Black&family=Archivo:wght@500&family=Arimo:wght@700&display=swap" rel="stylesheet">
<style>
  :root {
    --page-bg: #e4e4e4;
    --sign-bg: #e8e8e8;
    --brand-blue: #034a9b;
    --brand-grey: #55565a;
    --brand-orange: #f25305;
    --social-dot: #4a6aa5;
    --logo-tone-a: #d6d8de;
    --logo-tone-b: #cdd3e0;
    --white: #ffffff;
  }
  * { margin: 0; padding: 0; box-sizing: border-box; }
  html, body {
    width: 1200px; height: 1200px; overflow: hidden;
    background: var(--page-bg);
  }
  .sign {
    position: absolute; left: 31px; top: 398px;
    width: 1138px; height: 398px;
    background: var(--sign-bg);
    font-family: "Archivo Black", "Arial Black", sans-serif;
  }
  .logo-area {
    position: absolute; left: 460px; top: 22px;
    width: 217px; height: 128px;
    background: linear-gradient(135deg, var(--logo-tone-a), var(--logo-tone-b));
  }
  .company-name {
    position: absolute; left: 0; right: 0; top: 181px;
    text-align: center;
    font-size: 29px; line-height: 1; letter-spacing: 0.5px;
    color: var(--brand-grey);
    font-weight: 400;
  }
  .tagline {
    position: absolute; left: 0; right: 0; top: 221px;
    display: flex; justify-content: center; align-items: center; gap: 11px;
    font-family: "Archivo", Arial, sans-serif; font-weight: 500;
    font-size: 12.5px; letter-spacing: 1.6px;
    color: var(--brand-orange);
  }
  .tagline .rule { width: 60px; height: 1.5px; background: var(--brand-orange); }
  .services {
    position: absolute; left: 0; top: 258px; width: 1138px; height: 60px;
  }
  .service {
    position: absolute; top: 0; height: 52px;
    display: flex; align-items: center; justify-content: center;
    transform: translateX(-50%);
    text-align: center; white-space: nowrap;
    font-size: 25px; line-height: 0.98; letter-spacing: 0.3px;
    color: var(--brand-blue);
  }
  .divider {
    position: absolute; top: 4px; width: 1.5px; height: 45px;
    background: var(--brand-orange);
  }
  .footer-band {
    position: absolute; left: 0; bottom: 0; width: 1138px; height: 70px;
    background: var(--brand-blue);
  }
  .follow-tab {
    position: absolute; left: 0; top: 6px; width: 290px; height: 58px;
  }
  .follow-tab svg { position: absolute; inset: 0; }
  .follow-label {
    position: absolute; left: 45px; top: 11px;
    font-family: "Arimo", Arial, sans-serif; font-weight: 700;
    font-size: 34px; line-height: 1; color: var(--white);
  }
  .social-dot {
    position: absolute; left: 220px; top: 10px;
    width: 38px; height: 38px; border-radius: 50%;
    background: var(--social-dot);
  }
  .website {
    position: absolute; left: 404px; right: 77px; top: 17px;
    text-align: center;
    font-size: 33px; line-height: 1; letter-spacing: 0.5px;
    color: var(--white);
  }
</style>
</head>
<body>
  <section class="sign">
    <div class="logo-area" role="img" aria-label="Voltaris Span Services logo"></div>
    <h1 class="company-name">VOLTARIS SPAN SERVICES</h1>
    <div class="tagline">
      <span class="rule"></span>
      <span>INDUSTRIAL ELECTRICAL AND MECHANICAL SERVICES</span>
      <span class="rule"></span>
    </div>

    <div class="services">
      <div class="service" style="left:229px">INDUSTRIAL<br>AUTOMATION</div>
      <span class="divider" style="left:345px"></span>
      <div class="service" style="left:455px">ELECTRICAL</div>
      <span class="divider" style="left:566px"></span>
      <div class="service" style="left:683px">MECHANICAL<br>PROJECTS</div>
      <span class="divider" style="left:797px;height:55px"></span>
      <div class="service" style="left:912px">BREAKDOWNS</div>
    </div>

    <div class="footer-band">
      <div class="follow-tab">
        <svg width="290" height="58" viewBox="0 0 290 58">
          <polygon points="0,0 280,0 290,29 280,58 0,58" fill="var(--brand-orange)"/>
        </svg>
        <span class="follow-label">Follow Us</span>
        <span class="social-dot"></span>
      </div>
      <div class="website">www.voltarispan.com.au</div>
    </div>
  </section>
</body>
</html>
```